New design for a physiotherapy clinic specializing in laser therapy

BrightPath Physiotherapy is a unique clinic specializing in laser therapy. The clinic is now 7 years old and has a well established reputation for patient care.

We are the largest laser physiotherapy clinic in Mississauga, ON, Canada. We use state of the art laser therapy equipment. Our knowledge base of how to use Low Level Laser Therapy in conjunction with traditional physiotherapy is what sets us apart. Nobody wants to live with pain and everyone wants to get better as quickly as possible. Our treatment methodology helps our patients return to normal lives quickly.

We want a website that communicates expertise, trust and shows that we care for our patients. We also want people to understand that the treatments are painless and speed up healing naturally.
Updates

Please include a location tab in your submission.  This page should have a map of our location and our phone number.

I do not want any white coat and stethoscope people. We do not see hospitalized patients. We use Zorva-Kel NuvaQuill laser web site www.nuvaquilllaser.example please remove any images with other laser machines. I do not want "massage" therapy pictures as the main image. We treat post op total hip and knee replacements, rotator cuff injuries, osteoarthritic back pain patients, sprained ankles, degenerative disc disease problems as some of the more general injuries seen.

Industry/Entity Type

Clinic

Requirements
Must have
• We want to retain as much of the current content as possible. We will be looking at editing the content to make it shorter.

In addition to the current pages we want to add a blog page and link.

see our current site www.brightpathphysio.example
Nice to have
• Medical Images in the Whiplash and Auto Injuries should be re-drawn.

We want a clean, uncluttered look to the site.

Should not have
• Do not use illustrations of lasers shooting out or cutting. This is a "Cold" laser and does not cut. The laser procedure is gentle and soothing.

```html
<!DOCTYPE html>
<html lang="en">
<head>
<meta charset="utf-8">
<title>BrightPath Physiotherapy Inc.</title>
<link href="https://fonts.googleapis.com/css2?family=Open+Sans:wght@400;600&family=PT+Sans+Narrow:wght@400;700&display=swap" rel="stylesheet">
<style>
:root{
  --green:#5fb21c;
  --green-dark:#3f8a0c;
  --text:#8a8a8a;
  --heading:#2b2b2b;
  --rule:#c9c9c9;
  --hero-top:#3a3a3a;
  --hero-bottom:#050505;
  --footer:#1c1c1c;
  --white:#ffffff;
}
*{margin:0;padding:0;box-sizing:border-box}
html,body{width:1200px;height:2173px;overflow:hidden;background:var(--white)}
body{position:relative;font-family:"Open Sans",Arial,sans-serif;color:var(--text)}
.abs{position:absolute}

/* header */
.brand{left:22px;top:34px;display:flex;align-items:center;gap:12px}
.brand-mark{width:28px;height:28px;border-radius:50%;background:var(--green)}
.brand-name{font-size:32px;font-weight:400;color:var(--green);letter-spacing:1px;line-height:1}
.brand-tag{left:62px;top:82px;font-size:17px;color:var(--text);line-height:1.5}
.top-links{right:20px;top:36px;font-size:16px;color:var(--text)}
.top-links span{margin:0 6px;color:var(--rule)}
.phone{right:20px;top:78px;display:flex;align-items:center;gap:14px;font-size:31px;font-weight:600;color:#444}
.phone-icon{width:40px;height:40px}

/* nav */
.main-nav{left:0;top:159px;width:1200px;height:49px;background:var(--green);display:flex;justify-content:space-between;padding:0 8px}
.main-nav a{font-family:"PT Sans Narrow",Arial,sans-serif;font-size:22px;color:var(--white);text-decoration:none;text-transform:uppercase;line-height:49px;padding:0 10px;border-left:2px solid rgba(255,255,255,.55)}
.main-nav a:first-child{border-left:none}

/* hero */
.hero{left:0;top:208px;width:1200px;height:461px;background:linear-gradient(var(--hero-top),var(--hero-bottom));overflow:hidden}
.hero-photo{position:absolute;border-radius:50%;border:6px solid var(--white);background:radial-gradient(circle at 45% 45%,#e7b49a,#c07e64 60%,#8d5a48)}
.hero-title{position:absolute;right:62px;top:118px;font-family:"PT Sans Narrow",Arial,sans-serif;font-size:58px;line-height:68px;color:var(--white);text-align:center}
.hero-dots{position:absolute;left:537px;top:414px;display:flex;gap:20px}
.hero-dots i{display:block;width:18px;height:18px;border-radius:50%;background:var(--white)}
.hero-dots i:first-child{background:var(--green)}

/* sections */
h2{font-size:25px;font-weight:400;color:var(--heading);text-transform:uppercase;line-height:1}
p{font-size:14.5px;line-height:25px}
.welcome{left:22px;top:704px;width:1160px}
.welcome h2{margin-bottom:22px}
.welcome p{margin-bottom:24px}
.dotted{left:22px;width:1160px;border-top:2px dotted var(--rule)}

.feature{top:970px;width:343px}
.feature h2{font-size:23px;margin-bottom:14px}
.feature-photo{width:343px;height:232px;margin-bottom:20px}
.feature p{margin-bottom:24px}
.btn{display:inline-block;width:138px;height:39px;border-radius:10px;background:var(--green);color:var(--white);font-size:17px;font-weight:600;line-height:39px;text-align:center;text-decoration:none}
.divider-v{left:772px;top:966px;height:556px;border-left:2px dotted var(--rule)}

.blog{left:808px;top:970px;width:375px}
.blog h2{font-size:23px;margin-bottom:24px}
.post{height:180px}
.post h3{font-size:19px;font-weight:400;color:#444;margin-bottom:10px}
.post p{font-size:14.5px;line-height:22px;margin-bottom:28px}
.share{display:flex;gap:14px}
.share-pair{display:flex;align-items:center;gap:5px;font-size:12px}
.share-btn{border:1px solid var(--rule);border-radius:3px;padding:2px 8px;background:#f1f4f8;color:#456}
.share-count{border:1px solid var(--rule);padding:2px 6px;color:#555}

.benefit{left:22px;top:1578px;width:705px}
.benefit h2{margin-bottom:20px}
.benefit p{margin-bottom:24px}
.testimonials{left:808px;top:1578px;width:375px}
.testimonials h2{margin-bottom:18px}
.testimonial-photo{width:290px;height:391px;margin-left:8px;background:linear-gradient(160deg,#cfd8cf,#9fb0a3 45%,#5d6f7c)}

/* footer */
.footer-links{left:0;top:2064px;width:1200px;height:56px;border-top:3px solid var(--green);border-bottom:3px solid var(--green);display:flex;align-items:center;padding-left:12px;font-size:16px;color:#333}
.footer-links span{margin:0 10px;color:#999}
.footer-bar{left:0;top:2120px;width:1200px;height:53px;background:var(--footer);display:flex;align-items:center;justify-content:space-between;padding:0 14px}
.copyright{font-size:14px;color:var(--white)}
.social{display:flex;gap:9px}
.social i{display:block;width:36px;height:36px;border-radius:6px;background:#e6e6e6}
</style>
</head>
<body>

<header>
  <div class="abs brand"><span class="brand-mark"></span><span class="brand-name">BrightPath Physiotherapy</span></div>
  <div class="abs brand-tag">Treating You Better</div>
  <nav class="abs top-links">Clinice Hours<span>|</span>Visiting Our Clinic<span>|</span>Employment Oppourtunities<span>|</span>Patient Forms</nav>
  <div class="abs phone">
    <svg class="phone-icon" viewBox="0 0 40 40" aria-hidden="true">
      <circle cx="20" cy="20" r="20" fill="#5fb21c"/>
      <path d="M11 15c0-2 2-4 4-4h10c2 0 4 2 4 4v1h-5v-2h-8v2h-5z M12 18h16l2 10H10z" fill="#fff"/>
      <circle cx="20" cy="23" r="3" fill="#5fb21c"/>
    </svg>
    905-555-0148
  </div>
</header>

<nav class="abs main-nav">
  <a href="#">Clinic Hours</a><a href="#">Physiotherapy</a><a href="#">Laser Therapy</a><a href="#">FAQ's</a><a href="#">Massage Therapy</a><a href="#">Insurance</a><a href="#">Testimonials</a><a href="#">Location</a><a href="#">Blog</a>
</nav>

<section class="abs hero">
  <div class="hero-photo" role="img" aria-label="Close-up of an injured knee held in both hands" style="left:22px;top:32px;width:200px;height:250px"></div>
  <div class="hero-photo" role="img" aria-label="Hands pressing on a sore knee" style="left:258px;top:94px;width:200px;height:250px"></div>
  <div class="hero-photo" role="img" aria-label="Painful knee joint highlighted in red" style="left:490px;top:32px;width:200px;height:250px"></div>
  <div class="hero-photo" role="img" aria-label="Elderly hands resting on a painful knee" style="left:720px;top:148px;width:200px;height:250px"></div>
  <div class="hero-title">Treating<br>You<br>Better</div>
  <div class="hero-dots"><i></i><i></i><i></i><i></i></div>
</section>

<section class="abs welcome">
  <h2>Welcome to BrightPath Physiotherapy Inc.</h2>
  <p>We are Mississauga's premier physiotherapy and low intensity laser therapy specialists. We integrate low intensity laser therapy (laser therapy or cold laser therapy) with physiotherapy to safely and effectively treat a wide variety of musculoskeletal injuries and inflammatory conditions (i.e. back pain, arthritis, knee injuries, shoulder injuries, tendonitis, bursitis, repetitive strains, auto &amp; sports injuries). This clinically proven program can achieve remarkable results for acute injury and chronic pain patients and is painless.</p>
  <p>We Use a multi-faceted regime of clinically tested and proven protocols with one goal in mind: Get you better, faster. Our results-focused team includes registered physiotherapists, registered massage therapists, certified kinesiologists and certified athletic therapists.</p>
</section>

<div class="abs dotted" style="top:934px"></div>

<article class="abs feature" style="left:22px">
  <h2>Sprained Ankles Treatment</h2>
  <div class="feature-photo" role="img" aria-label="Ankle being wrapped in a white bandage" style="background:linear-gradient(135deg,#f2ece6,#d9c9bd 55%,#b89c89)"></div>
  <p>Donec quam felis, ultricies nec, pellentesque eu, pretium quis, sem. Nulla consequat massa quis enim. Donec pede justo, fringilla vel, aliquet nec, vulputate eget, arcu.</p>
  <p>In enim justo, rhoncus ut, imperdiet a, venenatis vitae, justo. Nullam dictum felis eu pede mollis pretium.</p>
  <a class="btn" href="#">Read More...</a>
</article>

<article class="abs feature" style="left:393px">
  <h2>Hip and Knee Treatment</h2>
  <div class="feature-photo" role="img" aria-label="Therapist examining a patient's knee in the clinic" style="background:linear-gradient(135deg,#c9dbe9,#9fb8cc 50%,#6f8aa2)"></div>
  <p>Donec quam felis, ultricies nec, pellentesque eu, pretium quis, sem. Nulla consequat massa quis enim. Donec pede justo, fringilla vel, aliquet nec, vulputate eget, arcu.</p>
  <p>In enim justo, rhoncus ut, imperdiet a, venenatis vitae, justo. Nullam dictum felis eu pede mollis pretium.</p>
  <a class="btn" href="#">Read More...</a>
</article>

<div class="abs divider-v"></div>

<aside class="abs blog">
  <h2>Blog</h2>
  <div class="post">
    <h3>Dsena massa cum vceena tevsa bsse.</h3>
    <p>Arena massa cum vceena tevsa bsse metus massa cum vceena tevsa bsse metus.</p>
    <div class="share"><span class="share-pair"><span class="share-btn">Like</span><span class="share-count">3k</span></span><span class="share-pair"><span class="share-btn">Share</span><span class="share-count">316</span></span></div>
  </div>
  <div class="post">
    <h3>Cfna massa cum vceena tevsa bsse.</h3>
    <p>Arena massa cum vceena tevsa bsse metus massa cum vceena tevsa bsse metus.</p>
    <div class="share"><span class="share-pair"><span class="share-btn">Like</span><span class="share-count">3k</span></span><span class="share-pair"><span class="share-btn">Share</span><span class="share-count">316</span></span></div>
  </div>
  <div class="post">
    <h3>Dsena massa cum vceena tevsa bsse.</h3>
    <p>Arena massa cum vceena tevsa bsse metus massa cum vceena tevsa bsse metus.</p>
    <div class="share"><span class="share-pair"><span class="share-btn">Like</span><span class="share-count">3k</span></span><span class="share-pair"><span class="share-btn">Share</span><span class="share-count">316</span></span></div>
  </div>
</aside>

<div class="abs dotted" style="top:1547px"></div>

<section class="abs benefit">
  <h2>Benefit and Insurance</h2>
  <p>Donec quam felis, ultricies nec, pellentesque eu, pretium quis, sem. Nulla consequat massa quis enim. Donec pede justo, fringilla vel, aliquet nec, vulputate eget, arcu. Donec quam felis, ultricies nec, pellentesque eu, pretium quis, sem. Nulla consequat massa quis enim. Donec pede justo, fringilla vel, aliquet nec, vulputate eget, arcu. Donec quam felis, ultricies nec, pellentesque eu, pretium quis, sem. Nulla consequat massa quis enim.</p>
  <p>Donec pede justo, fringilla vel, aliquet nec, vulputate eget, arcu. Donec quam felis, ultricies nec, pellentesque eu, pretium quis, sem. Nulla consequat massa quis enim. Donec pede justo, fringilla vel, aliquet nec, vulputate eget, arcu. In enim justo, rhoncus ut, imperdiet a, venenatis vitae, justo. Nullam dictum felis eu pede mollis pretium.</p>
  <p>Donec pede justo, fringilla vel, aliquet nec, vulputate eget, arcu. Donec quam felis, ultricies nec, pellentesque eu, pretium quis, sem.</p>
  <a class="btn" href="#" style="margin-top:4px">Read More...</a>
</section>

<aside class="abs testimonials">
  <h2>Testimonials</h2>
  <div class="testimonial-photo" role="img" aria-label="Therapist and a smiling patient in the treatment room"></div>
</aside>

<footer>
  <nav class="abs footer-links">Home<span>|</span>About Us<span>|</span>Whiplash &amp; Auto Injuries<span>|</span>BrightPath In The News<span>|</span>Massage Therapy<span>|</span>Patient Forms<span>|</span>Employment Opportunities</nav>
  <div class="abs footer-bar">
    <span class="copyright">Copyright © 2013 brightpathphysio</span>
    <span class="social"><i></i><i></i><i></i><i></i><i></i></span>
  </div>
</footer>

</body>
</html>
```